Sales Website Design

Create a sales-oriented website to advertise turn-key solutions for providing infection control to senior housing operators. There are several items uploaded. The pdf should serve as your guide. The powerpoint presentation has additional information.

The idea is this is senior housing reimagined for infection control. The design should be sleek, clean, vibrant and energetic.

Our goal is to sell a turnkey solution for making buildings safer for residents, staff, and families.

Target Market(s)

People who own and operate senior housing communities

Coding

Coded - Design and coding required

Number of Pages Required

5+ page

```html
<!DOCTYPE html>
<html lang="en">
<head>
<meta charset="utf-8">
<title>Crestline – Infection Control for Senior Housing</title>
<link rel="stylesheet" href="https://fonts.googleapis.com/css2?family=Roboto:wght@400;500;700;900&display=swap">
<style>
:root{
  --orange:#f2561d;
  --orange-dark:#d9461a;
  --ink:#222222;
  --text:#555555;
  --muted:#8a8a8a;
  --grey-bg:#efefef;
  --line:#cfcfcf;
  --footer:#062a2b;
  --footer-text:#c9d3d3;
  --white:#ffffff;
}
*{box-sizing:border-box;margin:0;padding:0}
html,body{width:1200px;height:3612px;overflow:hidden}
body{font-family:"Roboto",Arial,sans-serif;color:var(--text);background:var(--white);position:relative}
.abs{position:absolute}
.btn{display:inline-block;background:var(--orange);color:var(--white);font-weight:700;font-size:14px;letter-spacing:.5px;text-transform:uppercase;border-radius:22px;padding:13px 28px}

/* header */
.site-header{position:absolute;top:0;left:0;width:1200px;height:88px;background:var(--white)}
.brand{position:absolute;left:100px;top:22px;display:flex;align-items:center;gap:14px;font-size:40px;font-weight:700;letter-spacing:7px;color:var(--ink)}
.brand .mark{width:30px;height:30px;background:var(--orange)}
.topbar{position:absolute;right:110px;top:8px;display:flex;gap:26px;font-size:14px;font-weight:700;color:var(--ink)}
.topbar span{display:flex;align-items:center;gap:7px}
.main-nav{position:absolute;right:110px;top:52px;display:flex;gap:22px;font-size:14px;font-weight:700;color:var(--ink)}
.main-nav .active{color:var(--orange);border-bottom:2px solid var(--orange);padding-bottom:4px}

/* hero */
.hero{position:absolute;top:88px;left:0;width:1200px;height:472px;background:linear-gradient(100deg,#7c8a8e 0%,#a9b3ad 40%,#c7b69a 75%,#9aa39a 100%)}
.hero h1{position:absolute;left:108px;top:86px;width:560px;font-size:56px;line-height:66px;font-weight:700;color:var(--white)}
.hero .btn{position:absolute;left:108px;top:330px}
.hero .arrow{position:absolute;top:220px}
.hero .dots{position:absolute;left:560px;top:442px;display:flex;gap:10px}
.hero .dots i{width:10px;height:10px;border-radius:50%;background:rgba(255,255,255,.6)}
.hero .dots i.on{background:var(--white)}

/* welcome */
.welcome{position:absolute;top:560px;left:0;width:1200px;height:500px}
.welcome h2{position:absolute;left:108px;top:60px;font-size:46px;line-height:52px;font-weight:700;color:var(--ink)}
.welcome p{position:absolute;left:108px;width:420px;font-size:15px;line-height:24px;color:var(--muted)}
.welcome .btn{position:absolute;left:108px;top:390px}
.video{position:absolute;left:598px;top:90px;width:494px;height:282px;background:linear-gradient(180deg,#8fb3d8 0%,#c9d9e6 50%,#8ea07c 100%)}
.video svg{position:absolute;left:217px;top:111px}

/* why */
.why{position:absolute;top:1060px;left:0;width:1200px;height:360px;background:var(--grey-bg)}
.section-title{position:absolute;left:0;width:1200px;text-align:center;font-size:46px;font-weight:700;color:var(--ink)}
.why .section-title{top:40px}
.features{position:absolute;top:130px;left:120px;width:960px;display:flex;justify-content:space-between}
.feature{width:176px;text-align:center}
.feature h3{font-size:20px;font-weight:500;color:var(--ink);margin-top:16px}
.feature p{font-size:13px;line-height:18px;color:var(--muted);margin-top:8px}

/* products */
.products{position:absolute;top:1420px;left:0;width:1200px;height:800px}
.products .section-title{top:70px}
.product{position:absolute;width:432px;height:240px}
.product .label{position:absolute;left:0;bottom:0;width:300px;height:40px;background:var(--orange);color:var(--white);font-size:22px;font-weight:500;line-height:40px;text-align:center}

/* technology */
.tech{position:absolute;top:2220px;left:0;width:1200px;height:480px}
.tech-photo{position:absolute;left:0;top:8px;width:770px;height:470px;background:linear-gradient(110deg,#d8d2c6 0%,#b8b2a5 45%,#98a58a 70%,#e2ddd2 100%)}
.tech-box{position:absolute;left:690px;top:50px;width:400px;height:390px;background:var(--orange);color:var(--white);padding:30px 42px}
.tech-box h2{font-size:48px;font-weight:700}
.tech-box ul{list-style:none;margin-top:18px}
.tech-box li{font-size:19px;line-height:36px;display:flex;align-items:center;gap:12px}
.tech-box .btn{background:var(--white);color:var(--orange);margin-top:26px}

/* contact */
.contact{position:absolute;top:2700px;left:0;width:1200px;height:500px}
.contact .section-title{top:60px}
.field{position:absolute;border:1px solid var(--line);height:48px;font-size:15px;color:#888;padding:14px 12px;background:var(--white)}
.contact .btn{position:absolute;left:540px;top:436px;padding:13px 34px}

/* footer */
.site-footer{position:absolute;top:3200px;left:0;width:1200px;height:412px;background:var(--footer);color:var(--footer-text)}
.site-footer .brand{top:150px;color:var(--white);font-size:46px;letter-spacing:9px}
.site-footer .badge{position:absolute;left:574px;top:-26px;width:52px;height:52px;border-radius:50%;background:var(--footer);border:3px solid var(--white)}
.footer-col{position:absolute;top:112px;font-size:14px;line-height:24px}
.footer-col h4{color:var(--white);font-size:16px;font-weight:700;margin-bottom:10px}
.footer-col .row{display:flex;gap:10px;align-items:flex-start;margin-bottom:26px}
.social{position:absolute;right:110px;top:340px;display:flex;gap:12px}
.social i{width:34px;height:34px;border-radius:50%;background:var(--white)}
.copyright{position:absolute;left:100px;top:380px;font-size:13px;color:var(--footer-text)}
.footer-rule{position:absolute;left:0;top:330px;width:1200px;height:1px;background:rgba(255,255,255,.12)}
</style>
</head>
<body>

<header class="site-header">
  <div class="brand"><span class="mark"></span>CRESTLINE</div>
  <div class="topbar">
    <span><svg width="14" height="14" viewBox="0 0 24 24"><path fill="#f2561d" d="M6.6 10.8c1.4 2.8 3.8 5.2 6.6 6.6l2.2-2.2c.3-.3.7-.4 1-.2 1.1.4 2.3.6 3.6.6.6 0 1 .4 1 1V20c0 .6-.4 1-1 1C10.6 21 3 13.4 3 4c0-.6.4-1 1-1h3.5c.6 0 1 .4 1 1 0 1.3.2 2.5.6 3.6.1.3 0 .7-.2 1z"/></svg>1 555 010 0199</span>
    <span><svg width="16" height="12" viewBox="0 0 16 12"><rect width="16" height="12" rx="1" fill="#f2561d"/><path d="M1 1l7 6 7-6" stroke="#fff" stroke-width="1.5" fill="none"/></svg>info@crestline-care.com</span>
  </div>
  <nav class="main-nav">
    <span class="active">HOME</span><span>ABOUT</span><span>SERVICES</span><span>PRODUCTS</span><span>TECHNOLOGY</span><span>CONTACT US</span>
  </nav>
</header>

<section class="hero" role="img" aria-label="Photo of a senior couple walking outside a palm-lined senior housing community">
  <h1>Providing Infection Control To Senior Housing Operators</h1>
  <span class="btn">Get More Info</span>
  <svg class="arrow" style="left:24px" width="20" height="34" viewBox="0 0 20 34"><path d="M17 3L3 17l14 14" stroke="#fff" stroke-width="4" fill="none"/></svg>
  <svg class="arrow" style="left:1156px" width="20" height="34" viewBox="0 0 20 34"><path d="M3 3l14 14L3 31" stroke="#fff" stroke-width="4" fill="none"/></svg>
  <div class="dots"><i class="on"></i><i></i><i></i></div>
</section>

<section class="welcome">
  <h2>WELCOME TO<br>CRESTLINE</h2>
  <p style="top:190px">Our turnkey program brings hospital grade infection control to senior living communities, so residents, staff and families feel safe every day.</p>
  <p style="top:280px">We plan, install and maintain every system, from touchless entry to air sanitation, with one partner and one simple monthly plan.</p>
  <span class="btn">Read More</span>
  <div class="video" role="img" aria-label="Video still of a modern senior housing building under a blue sky">
    <svg width="60" height="60" viewBox="0 0 60 60"><circle cx="30" cy="30" r="30" fill="#222" fill-opacity=".85"/><path d="M24 18l18 12-18 12z" fill="#fff"/></svg>
  </div>
</section>

<section class="why">
  <h2 class="section-title">WHY CHOOSE CRESTLINE</h2>
  <div class="features">
    <div class="feature">
      <svg width="150" height="110" viewBox="0 0 150 110"><path d="M75 6L144 104H6z" fill="none" stroke="#8a8a8a" stroke-width="6" stroke-linejoin="round"/><circle cx="75" cy="64" r="9" fill="#f2561d"/><circle cx="56" cy="70" r="7" fill="#f2561d"/><circle cx="94" cy="70" r="7" fill="#f2561d"/><rect x="48" y="80" width="54" height="10" rx="5" fill="#f2561d"/></svg>
      <h3>Customized</h3><p>Tailored to your building and your residents</p>
    </div>
    <div class="feature">
      <svg width="150" height="110" viewBox="0 0 150 110"><path d="M6 6H144L75 104z" fill="none" stroke="#8a8a8a" stroke-width="6" stroke-linejoin="round"/><rect x="55" y="24" width="40" height="26" rx="3" fill="none" stroke="#f2561d" stroke-width="4"/><circle cx="75" cy="37" r="6" fill="#f2561d"/></svg>
      <h3>Affordable</h3><p>Clear pricing that fits your budget</p>
    </div>
    <div class="feature">
      <svg width="150" height="110" viewBox="0 0 150 110"><path d="M75 6L144 104H6z" fill="none" stroke="#8a8a8a" stroke-width="6" stroke-linejoin="round"/><path d="M62 92l22-22" stroke="#f2561d" stroke-width="7" stroke-linecap="round"/><circle cx="88" cy="62" r="10" fill="none" stroke="#f2561d" stroke-width="5"/></svg>
      <h3>Easily Installed</h3><p>Quick setup with no disruption</p>
    </div>
    <div class="feature">
      <svg width="150" height="110" viewBox="0 0 150 110"><path d="M6 6H144L75 104z" fill="none" stroke="#8a8a8a" stroke-width="6" stroke-linejoin="round"/><circle cx="68" cy="34" r="9" fill="none" stroke="#f2561d" stroke-width="5"/><circle cx="86" cy="46" r="6" fill="none" stroke="#f2561d" stroke-width="4"/></svg>
      <h3>High Technology</h3><p>Smart sensors and real time data</p>
    </div>
    <div class="feature">
      <svg width="150" height="110" viewBox="0 0 150 110"><path d="M75 6L144 104H6z" fill="none" stroke="#8a8a8a" stroke-width="6" stroke-linejoin="round"/><path d="M75 50l18 6v12c0 10-8 17-18 20-10-3-18-10-18-20V56z" fill="#f2561d"/><rect x="72" y="58" width="6" height="22" fill="#fff"/></svg>
      <h3>Increased Safety</h3><p>Fewer risks for every resident</p>
    </div>
  </div>
</section>

<section class="products">
  <h2 class="section-title">OUR PRODUCTS</h2>
  <div class="product" style="left:166px;top:220px;background:linear-gradient(135deg,#c9c2b6,#8f8a80)" role="img" aria-label="Photo of a resident lounge with branded signage">
    <div class="label">Branded Signage</div>
  </div>
  <div class="product" style="left:610px;top:220px;background:linear-gradient(135deg,#cfd3d6,#9aa1a6)" role="img" aria-label="Photo of hands under a touchless dispenser">
    <div class="label">Touchless Options</div>
  </div>
  <div class="product" style="left:166px;top:480px;background:linear-gradient(135deg,#e4e7ea,#9eb0bd)" role="img" aria-label="Photo of an air sanitation unit">
    <div class="label">Air Sanitation</div>
  </div>
  <div class="product" style="left:610px;top:480px;background:linear-gradient(135deg,#8a8c8e,#3c3f42)" role="img" aria-label="Photo of clear custom dividers between desks">
    <div class="label">Custom Dividers</div>
  </div>
</section>

<section class="tech">
  <div class="tech-photo" role="img" aria-label="Photo of a senior couple relaxing on a sofa at home"></div>
  <div class="tech-box">
    <h2>TECHNOLOGY</h2>
    <ul>
      <li><svg width="18" height="18" viewBox="0 0 18 18"><circle cx="9" cy="9" r="9" fill="#fff"/><path d="M5 9l3 3 5-6" stroke="#f2561d" stroke-width="2" fill="none"/></svg>Touchless Temperature Scans</li>
      <li><svg width="18" height="18" viewBox="0 0 18 18"><circle cx="9" cy="9" r="9" fill="#fff"/><path d="M5 9l3 3 5-6" stroke="#f2561d" stroke-width="2" fill="none"/></svg>Wireless Diagnostic equipment</li>
      <li><svg width="18" height="18" viewBox="0 0 18 18"><circle cx="9" cy="9" r="9" fill="#fff"/><path d="M5 9l3 3 5-6" stroke="#f2561d" stroke-width="2" fill="none"/></svg>Wearable Monitoring</li>
      <li><svg width="18" height="18" viewBox="0 0 18 18"><circle cx="9" cy="9" r="9" fill="#fff"/><path d="M5 9l3 3 5-6" stroke="#f2561d" stroke-width="2" fill="none"/></svg>Disinfectant Equipment</li>
      <li><svg width="18" height="18" viewBox="0 0 18 18"><circle cx="9" cy="9" r="9" fill="#fff"/><path d="M5 9l3 3 5-6" stroke="#f2561d" stroke-width="2" fill="none"/></svg>UV Sanitation Devices</li>
    </ul>
    <span class="btn">Read More</span>
  </div>
</section>

<section class="contact">
  <h2 class="section-title">CONTACT US</h2>
  <div class="field" style="left:180px;top:136px;width:410px">First Name</div>
  <div class="field" style="left:610px;top:136px;width:410px">Last Name</div>
  <div class="field" style="left:180px;top:200px;width:410px">Business</div>
  <div class="field" style="left:610px;top:200px;width:410px">Email</div>
  <div class="field" style="left:180px;top:264px;width:840px">Phone</div>
  <div class="field" style="left:180px;top:328px;width:840px;height:86px">How can we help?</div>
  <span class="btn">Submit</span>
</section>

<footer class="site-footer">
  <div class="badge"></div>
  <div class="brand"><span class="mark"></span>CRESTLINE</div>
  <div class="footer-col" style="left:518px">
    <h4>QUICK LINKS</h4>
    <div>Home</div><div>About</div><div>Services</div><div>Products</div><div>Technology</div><div>Contact Us</div>
  </div>
  <div class="footer-col" style="left:740px">
    <h4>CONTACT US</h4>
    <div class="row"><svg width="14" height="18" viewBox="0 0 14 18" style="margin-top:4px"><path d="M7 0a7 7 0 017 7c0 5-7 11-7 11S0 12 0 7a7 7 0 017-7z" fill="#c9d3d3"/><circle cx="7" cy="7" r="2.5" fill="#062a2b"/></svg><span>100 Harbor Lane, Suite 4<br>Springfield, ST 00000</span></div>
    <div class="row"><svg width="14" height="14" viewBox="0 0 24 24" style="margin-top:5px"><path fill="#c9d3d3" d="M6.6 10.8c1.4 2.8 3.8 5.2 6.6 6.6l2.2-2.2c.3-.3.7-.4 1-.2 1.1.4 2.3.6 3.6.6.6 0 1 .4 1 1V20c0 .6-.4 1-1 1C10.6 21 3 13.4 3 4c0-.6.4-1 1-1h3.5c.6 0 1 .4 1 1 0 1.3.2 2.5.6 3.6.1.3 0 .7-.2 1z"/></svg><span>1 555 010 0199</span></div>
    <div class="row"><svg width="16" height="12" viewBox="0 0 16 12" style="margin-top:6px"><rect width="16" height="12" rx="1" fill="#c9d3d3"/><path d="M1 1l7 6 7-6" stroke="#062a2b" stroke-width="1.5" fill="none"/></svg><span>info@crestline-care.com</span></div>
  </div>
  <div class="footer-rule"></div>
  <div class="social"><i></i><i></i><i></i></div>
  <div class="copyright">Copyright © 2020, Crestline. All rights reserved.</div>
</footer>

</body>
</html>
```